K7 Business Card Design for Professional IT Security Company

I have a small Cyber Security Startup and I need to have a business card designed.

My company specializes in: Government Risk Compliance, Cyber Security Assessments, Big Data

Please use my logo and fonts attached.

Industry/Entity Type

Information Technology

Contact Information for Business Card

Details
Dale Whitcomb, MS, CISSP
Member
(p) 555.518.3096
(e) dwhitcomb@k7vantagesys.net
(a) P.O. Box 863, Brindlemoor, ZZ 00186

K7 Vantage Systems
www.k7vantagesys.net

Font styles to use
Other font styles liked:
• Please see attached

```html
<!DOCTYPE html>
<html lang="en">
<head>
<meta charset="utf-8">
<title>K7 Vantage Systems — Business Card</title>
<link rel="stylesheet" href="https://fonts.googleapis.com/css2?family=Montserrat:wght@400;600&display=swap">
<style>
  :root {
    --backdrop: #2b2b2b;
    --card: #f4f4f4;
    --card-edge: #e2e2e2;
    --brand-blue: #1577bd;
    --brand-aqua: #1cb8d4;
    --ink: #4a4a4a;
    --ink-soft: #6b6b6b;
  }
  * { box-sizing: border-box; margin: 0; padding: 0; }
  html, body { width: 1200px; height: 834px; overflow: hidden; }
  body {
    background: var(--backdrop);
    font-family: "Montserrat", Arial, sans-serif;
    display: flex;
    align-items: center;
    justify-content: center;
    gap: 40px;
  }
  .card {
    width: 540px;
    height: 309px;
    background: var(--card);
    border: 1px solid var(--card-edge);
    box-shadow: 0 10px 30px rgba(0,0,0,.45);
    position: relative;
  }
  .card--front { display: flex; align-items: center; justify-content: center; }
  .brand {
    display: flex;
    align-items: center;
    gap: 10px;
    color: var(--brand-blue);
    font-weight: 600;
    font-size: 24px;
    letter-spacing: .5px;
  }
  .brand__dot {
    width: 18px; height: 18px; border-radius: 50%;
    background: var(--brand-aqua);
    flex: none;
  }
  .card--back .brand {
    position: absolute;
    left: 40px; top: 50%;
    transform: translateY(-50%);
    font-size: 19px;
    width: 210px;
    line-height: 1.25;
  }
  .contact {
    position: absolute;
    left: 280px; top: 72px;
    color: var(--ink);
  }
  .contact__name { font-weight: 600; font-size: 15px; }
  .contact__role { color: var(--brand-blue); font-size: 12px; margin: 2px 0 0 14px; }
  .contact__address { font-size: 11px; color: var(--ink-soft); margin: 16px 0 10px 14px; }
  .contact__list { list-style: none; font-size: 11px; color: var(--ink-soft); margin-left: 14px; }
  .contact__list li { display: flex; align-items: center; gap: 8px; margin-bottom: 5px; }
  .contact__list svg { width: 12px; height: 12px; flex: none; }
</style>
</head>
<body>
  <section class="card card--front">
    <div class="brand"><span class="brand__dot"></span><span>K7 Vantage Systems</span></div>
  </section>

  <section class="card card--back">
    <div class="brand"><span class="brand__dot"></span><span>K7 Vantage Systems</span></div>
    <div class="contact">
      <p class="contact__name">Dale Whitcomb, MS, CISSP</p>
      <p class="contact__role">Member</p>
      <p class="contact__address">P.O. Box 863, Brindlemoor, ZZ 00186</p>
      <ul class="contact__list">
        <li>
          <svg viewBox="0 0 12 12" aria-hidden="true"><path d="M2 4c0-2 8-2 8 0v1H8V4H4v1H2zM3 6h6l1 4H2z" fill="var(--brand-blue)"/></svg>
          <span>555.518.3096</span>
        </li>
        <li>
          <svg viewBox="0 0 12 12" aria-hidden="true"><rect x="1" y="2.5" width="10" height="7" fill="none" stroke="var(--brand-blue)" stroke-width="1.2"/><path d="M1 3l5 4 5-4" fill="none" stroke="var(--brand-blue)" stroke-width="1.2"/></svg>
          <span>dwhitcomb@k7vantagesys.net</span>
        </li>
        <li>
          <svg viewBox="0 0 12 12" aria-hidden="true"><circle cx="6" cy="6" r="4.7" fill="none" stroke="var(--brand-blue)" stroke-width="1.2"/><path d="M1.3 6h9.4M6 1.3c-2.5 3-2.5 6.4 0 9.4M6 1.3c2.5 3 2.5 6.4 0 9.4" fill="none" stroke="var(--brand-blue)" stroke-width="1"/></svg>
          <span>www.k7vantagesys.net</span>
        </li>
      </ul>
    </div>
  </section>
</body>
</html>
```